Hipster Hard Apple Cider - Bike / Gear / Cog Themed Label

Hard Apple Cider Label Needed:

- Looking for a retro, fun, funky, Venice Beach vibe.

- Design should incorporate bike/bicycle/wheel elements, appeal to both sexes and should be applicable to a can. (See can example in attachments).

- There should be a main brand logo that can stand alone in representing the brand and the feel of the brand. I envision a bike wheel, Sp*kes, gears, etc.

Please use brand name posted as JPG titled "Brand Name" in Attached Files:
>>> Brindle Cider

Target Market(s)

Our consumer is:
- Millennial
- Hipster
- Adventurous
- Active (biking/cycling)
- A craft beer + wine purchaser
- Unisex, veering towards masculine (65% male)

Industry/Entity Type

Wheel

Requirements
Must have
• - Bike elements that tie in the brand name (cogs, sp*kes, gears, bike frame, etc.)
• - A strong logo that can represent the brand

```html
<!DOCTYPE html>
<html lang="en">
<head>
<meta charset="utf-8">
<title>Brindle Cider – Dry Hard Apple Cider Label</title>
<link rel="stylesheet" href="https://fonts.googleapis.com/css2?family=Oswald:wght@400;500;600;700&family=Playfair+Display:wght@700&family=Vollkorn:ital,wght@1,700&display=swap">
<style>
  :root {
    --backdrop: #b2afa4;
    --ink: #2a2a2a;
    --line: #5a5a5a;
    --label: #ececec;
    --red: #e0262b;
    --ribbon-grey: #b3b3b3;
    --text-grey: #666666;
    --placeholder: #d2d2d2;
    --placeholder-faint: #e1e1e1;
    --white: #ffffff;
  }
  html, body {
    margin: 0;
    padding: 0;
    width: 1200px;
    height: 1034px;
    overflow: hidden;
    background: var(--backdrop);
  }
  .canvas {
    position: relative;
    width: 1200px;
    height: 1034px;
  }
  .brand-mark {
    position: absolute;
    top: 58px;
    left: 0;
    width: 1200px;
    text-align: center;
    font-family: "Oswald", sans-serif;
    font-weight: 700;
    font-size: 62px;
    letter-spacing: 1px;
    color: var(--ink);
    margin: 0;
    line-height: 1;
  }
  .label {
    position: absolute;
    top: 390px;
    width: 296px;
    height: 488px;
  }
  .label--front { left: 262px; }
  .label--back { left: 652px; }
  .label svg { display: block; }
  .sans { font-family: "Oswald", sans-serif; }
  .serif { font-family: "Playfair Display", serif; }
  .italic-serif { font-family: "Vollkorn", serif; font-style: italic; }
</style>
</head>
<body>
<main class="canvas">
  <h1 class="brand-mark">BRINDLE CIDER</h1>

  <!-- Front panel -->
  <section class="label label--front" aria-label="Front label">
    <svg width="296" height="488" viewBox="0 0 296 488">
      <rect class="label-ground" width="296" height="488" fill="var(--label)"/>

      <g class="top-rules" stroke="var(--line)" stroke-width="1">
        <line x1="8" y1="12" x2="288" y2="12"/>
        <line x1="8" y1="15" x2="288" y2="15"/>
      </g>

      <g class="brand-bar">
        <rect x="8" y="20" width="180" height="46" fill="var(--red)"/>
        <g stroke="var(--ink)" stroke-width="1">
          <line x1="160" y1="30" x2="184" y2="30"/>
          <line x1="160" y1="36" x2="184" y2="36"/>
          <line x1="160" y1="42" x2="184" y2="42"/>
          <line x1="160" y1="48" x2="184" y2="48"/>
          <line x1="160" y1="54" x2="184" y2="54"/>
        </g>
        <text class="sans" x="16" y="52" font-size="21" font-weight="600" fill="var(--white)">BRINDLE CIDER</text>
      </g>

      <g class="origin-box">
        <rect x="192" y="20" width="96" height="46" fill="var(--red)"/>
        <text class="sans" x="240" y="40" font-size="11" font-weight="500" fill="var(--white)" text-anchor="middle">MARLOW FLATS</text>
        <text class="sans" x="240" y="55" font-size="11" font-weight="500" fill="var(--white)" text-anchor="middle">CA</text>
      </g>

      <line class="dotted-rule" x1="8" y1="80" x2="288" y2="80" stroke="var(--ink)" stroke-width="2" stroke-dasharray="2 4"/>

      <rect class="upper-frame" x="8" y="92" width="280" height="70" fill="none" stroke="var(--line)" stroke-width="1"/>

      <rect x="22" y="106" width="40" height="44" rx="18" fill="var(--placeholder)" role="img" aria-label="Engraved apple illustration"/>
      <rect x="234" y="106" width="40" height="44" rx="18" fill="var(--placeholder)" role="img" aria-label="Engraved apple illustration"/>

      <path class="lower-frame" d="M8 172 H86 A62 44 0 0 0 210 172 H288 V466 H8 Z" fill="none" stroke="var(--line)" stroke-width="1"/>

      <circle cx="148" cy="150" r="54" fill="var(--placeholder)" role="img" aria-label="Bicycle wheel with spokes illustration"/>

      <g class="corner-ticks" stroke="var(--line)" stroke-width="1">
        <line x1="16" y1="180" x2="16" y2="194"/><line x1="20" y1="180" x2="20" y2="194"/><line x1="24" y1="180" x2="24" y2="190"/><line x1="28" y1="180" x2="28" y2="188"/>
        <line x1="280" y1="180" x2="280" y2="194"/><line x1="276" y1="180" x2="276" y2="194"/><line x1="272" y1="180" x2="272" y2="190"/><line x1="268" y1="180" x2="268" y2="188"/>
        <line x1="16" y1="444" x2="16" y2="458"/><line x1="20" y1="444" x2="20" y2="458"/><line x1="24" y1="448" x2="24" y2="458"/><line x1="28" y1="450" x2="28" y2="458"/>
        <line x1="280" y1="444" x2="280" y2="458"/><line x1="276" y1="444" x2="276" y2="458"/><line x1="272" y1="448" x2="272" y2="458"/><line x1="268" y1="450" x2="268" y2="458"/>
      </g>

      <g class="ribbon ribbon--hard">
        <polygon points="12,238 284,238 272,257 284,276 12,276 24,257" fill="var(--red)"/>
        <text class="serif" x="148" y="272" font-size="40" fill="var(--ink)" text-anchor="middle" letter-spacing="1">HARD</text>
      </g>

      <g class="ribbon ribbon--style">
        <polygon points="54,290 242,290 232,305 242,320 54,320 64,305" fill="var(--ribbon-grey)"/>
        <text class="italic-serif" x="148" y="314" font-size="27" fill="var(--text-grey)" text-anchor="middle">apple cider</text>
      </g>

      <g class="ribbon ribbon--dry">
        <polygon points="84,366 212,366 204,378 212,390 84,390 92,378" fill="var(--red)"/>
        <text class="serif" x="148" y="394" font-size="40" fill="var(--ink)" text-anchor="middle">DRY</text>
      </g>

      <g class="abv-tag">
        <rect x="104" y="446" width="88" height="16" fill="var(--red)"/>
        <text class="sans" x="148" y="458" font-size="10" font-weight="500" fill="var(--white)" text-anchor="middle">7% alc./vol.</text>
      </g>

      <line class="dotted-rule" x1="8" y1="476" x2="288" y2="476" stroke="var(--ink)" stroke-width="2" stroke-dasharray="2 4"/>
    </svg>
  </section>

  <!-- Back panel -->
  <section class="label label--back" aria-label="Back label">
    <svg width="296" height="488" viewBox="0 0 296 488">
      <rect class="label-ground" width="296" height="488" fill="var(--label)"/>

      <rect x="20" y="18" width="60" height="40" rx="6" fill="var(--placeholder)" role="img" aria-label="Cluster of gear cogs"/>
      <rect x="216" y="18" width="60" height="40" rx="6" fill="var(--placeholder)" role="img" aria-label="Cluster of gear cogs"/>

      <g class="brand-bar">
        <rect x="96" y="20" width="112" height="36" fill="var(--red)"/>
        <text class="sans" x="152" y="44" font-size="15" font-weight="600" fill="var(--white)" text-anchor="middle">BRINDLE CIDER</text>
      </g>

      <line class="dotted-rule" x1="8" y1="72" x2="288" y2="72" stroke="var(--ink)" stroke-width="2" stroke-dasharray="2 4"/>

      <rect x="20" y="210" width="256" height="190" rx="8" fill="var(--placeholder-faint)" role="img" aria-label="Faint pattern of interlocking gears"/>

      <rect class="upper-frame" x="8" y="82" width="280" height="60" fill="none" stroke="var(--line)" stroke-width="1"/>
      <path class="lower-frame" d="M8 152 H86 A62 46 0 0 0 210 152 H288 V466 H8 Z" fill="none" stroke="var(--line)" stroke-width="1"/>

      <g class="warning sans" font-size="8" fill="var(--ink)" text-anchor="middle">
        <text x="148" y="98">GOVERNMENT WARNING:</text>
        <text x="148" y="110">(1) ACCORDING TO THE SURGEON GENERAL, WOMEN SHOULD</text>
        <text x="148" y="120">NOT DRINK ALCOHOLIC BEVERAGES DURING PREGNANCY</text>
        <text x="148" y="130">BECAUSE OF THE RISK OF BIRTH DEFECTS.</text>
        <text x="148" y="146">(2) CONSUMPTION OF ALCOHOLIC</text>
        <text x="148" y="156">BEVERAGES IMPAIRS YOUR ABILITY</text>
        <text x="148" y="166">TO DRIVE A CAR OR OPERATE</text>
        <text x="148" y="176">MACHINERY, AND MAY</text>
        <text x="148" y="186">CAUSE HEALTH PROBLEMS.</text>
      </g>

      <g class="producer sans" fill="var(--ink)" text-anchor="middle">
        <text x="148" y="410" font-size="12">CONTAINS SULFITES</text>
        <text x="148" y="436" font-size="12">VINTED • BOTTLED BY BRINDLE CIDER</text>
        <text x="148" y="452" font-size="12">MARLOW FLATS, CA</text>
      </g>

      <line class="dotted-rule" x1="8" y1="476" x2="288" y2="476" stroke="var(--ink)" stroke-width="2" stroke-dasharray="2 4"/>
    </svg>
  </section>
</main>
</body>
</html>
```